Business Cards and Stationary
Corvane Echo Partners LLC
Use same font as used in my logo
Gerald Ashcombe, RDCS, RVT
Owner / Sonographer
42731 SE 118th Ave.
Marlow Springs, FL. 32587
Gerald.Ashcombe@corvanecho.net
WWW.CORVANECHO.NET
email is =
would not allow me to type this in for some reason

```html
<!DOCTYPE html>
<html lang="en">
<head>
<meta charset="utf-8">
<title>Corvane Echo Partners LLC – Stationery</title>
<link href="https://fonts.googleapis.com/css2?family=Orbitron:wght@600&family=Open+Sans:wght@400;600&display=swap" rel="stylesheet">
<style>
  :root{
    --bg:#ececec;
    --paper:#ffffff;
    --blue:#1f4f9c;
    --blue-deep:#143a7a;
    --green:#7cc242;
    --card-dark:#151515;
    --ink:#4a4a4a;
  }
  html,body{margin:0;padding:0;overflow:hidden}
  body{width:1200px;height:936px;background:var(--bg);position:relative;font-family:'Open Sans',sans-serif}
  .piece{position:absolute;background:var(--paper);box-shadow:0 2px 8px rgba(0,0,0,.18);overflow:hidden}
  .piece svg{display:block;width:100%;height:100%}
  .letterhead{left:253px;top:63px;width:317px;height:552px}
  .folder{left:633px;top:46px;width:495px;height:569px}
  .card-front{left:46px;top:653px;width:174px;height:111px}
  .card-back{left:46px;top:777px;width:174px;height:109px;background:var(--card-dark)}
  .envelope-front{left:253px;top:670px;width:317px;height:203px}
  .envelope-back{left:633px;top:670px;width:495px;height:203px}
  .brand{font-family:'Orbitron',sans-serif;font-weight:600;fill:var(--blue)}
  .small{font-family:'Open Sans',sans-serif;fill:#fff}
  .dark-small{font-family:'Open Sans',sans-serif;fill:var(--ink)}
  .url{font-family:'Orbitron',sans-serif;font-weight:600;fill:#fff;letter-spacing:2px}
</style>
</head>
<body>

<div class="piece letterhead">
  <svg viewBox="0 0 317 552">
    <defs>
      <linearGradient id="lhBlue" x1="0" y1="0" x2="1" y2="0">
        <stop offset="0" stop-color="var(--blue-deep)"/><stop offset="1" stop-color="var(--blue)"/>
      </linearGradient>
    </defs>
    <circle cx="112" cy="48" r="7" fill="var(--green)"/>
    <text class="brand" x="158.5" y="72" font-size="10" text-anchor="middle">CORVANE ECHO PARTNERS LLC</text>
    <path d="M0 466 C90 500 190 440 317 418 L317 552 L0 552 Z" fill="url(#lhBlue)"/>
    <path d="M0 458 C90 490 190 430 317 408" fill="none" stroke="var(--green)" stroke-width="4"/>
    <text class="small" x="16" y="504" font-size="6">42731 SE 118th Ave.</text>
    <text class="small" x="16" y="513" font-size="6">Marlow Springs, FL. 32587</text>
    <text class="small" x="16" y="522" font-size="6">Tel (352) 555-0143</text>
    <text class="small" x="16" y="531" font-size="6">Gerald.Ashcombe@corvanecho.net</text>
  </svg>
</div>

<div class="piece folder">
  <svg viewBox="0 0 495 569">
    <defs>
      <linearGradient id="fdBlue" x1="0" y1="0" x2="1" y2="0">
        <stop offset="0" stop-color="var(--blue-deep)"/><stop offset="1" stop-color="var(--blue)"/>
      </linearGradient>
    </defs>
    <circle cx="247.5" cy="210" r="14" fill="var(--green)"/>
    <text class="brand" x="247.5" y="262" font-size="17" text-anchor="middle">CORVANE ECHO PARTNERS</text>
    <text class="brand" x="247.5" y="282" font-size="11" text-anchor="middle">LLC</text>
    <path d="M0 468 C140 520 300 420 495 392 L495 569 L0 569 Z" fill="url(#fdBlue)"/>
    <path d="M0 458 C140 508 300 410 495 380" fill="none" stroke="var(--green)" stroke-width="6"/>
    <text class="url" x="247.5" y="540" font-size="9" text-anchor="middle">WWW.CORVANECHO.NET</text>
  </svg>
</div>

<div class="piece card-front">
  <svg viewBox="0 0 174 111">
    <circle cx="14" cy="18" r="4" fill="var(--green)"/>
    <text class="brand" x="22" y="21" font-size="5.6">CORVANE ECHO PARTNERS LLC</text>
    <text class="dark-small" x="100" y="40" font-size="5" font-weight="600">Gerald Ashcombe, RDCS, RVT</text>
    <text class="dark-small" x="100" y="47" font-size="4.2">Owner / Sonographer</text>
    <text class="dark-small" x="100" y="56" font-size="4.2">Tel (352) 555-0143</text>
    <path d="M0 92 C50 104 110 74 174 70 L174 111 L0 111 Z" fill="var(--blue)"/>
    <path d="M0 88 C50 100 110 70 174 66" fill="none" stroke="var(--green)" stroke-width="2"/>
    <text class="small" x="8" y="104" font-size="4">Gerald.Ashcombe@corvanecho.net</text>
  </svg>
</div>

<div class="piece card-back">
  <svg viewBox="0 0 174 109">
    <circle cx="40" cy="52" r="5" fill="var(--green)"/>
    <text class="brand" x="50" y="55" font-size="6">CORVANE ECHO PARTNERS LLC</text>
  </svg>
</div>

<div class="piece envelope-front">
  <svg viewBox="0 0 317 203">
    <circle cx="16" cy="20" r="5" fill="var(--green)"/>
    <text class="brand" x="26" y="24" font-size="7.5">CORVANE ECHO PARTNERS LLC</text>
    <text class="dark-small" x="26" y="36" font-size="4.5">42731 SE 118th Ave., Marlow Springs, FL. 32587</text>
    <path d="M0 176 C100 190 200 130 317 110 L317 203 L0 203 Z" fill="var(--blue)"/>
    <path d="M0 168 C100 182 200 122 317 102" fill="none" stroke="var(--green)" stroke-width="3"/>
  </svg>
</div>

<div class="piece envelope-back">
  <svg viewBox="0 0 495 203">
    <defs>
      <linearGradient id="evBlue" x1="0" y1="0" x2="0" y2="1">
        <stop offset="0" stop-color="var(--blue)"/><stop offset="1" stop-color="var(--blue-deep)"/>
      </linearGradient>
    </defs>
    <path d="M0 0 L495 0 L495 44 C400 70 320 80 247 80 C170 80 90 70 0 44 Z" fill="url(#evBlue)"/>
    <path d="M0 50 C90 76 170 86 247 86 C320 86 400 76 495 50" fill="none" stroke="var(--green)" stroke-width="2"/>
    <text class="url" x="247.5" y="32" font-size="8" text-anchor="middle">WWW.CORVANECHO.NET</text>
  </svg>
</div>

</body>
</html>
```